Greek Yogurt Design

Design Brief – Premium Greek Yogurt Line (150g Pot)
Background
We are a small-to-medium dairy producer launching a new premium Greek yogurt range. This line will come in slightly larger pots than our standard yogurts, and we are targeting an upmarket clientele with a higher price point.
Product Details
Product: Greek Yogurt (fruit on the bottom, yogurt on top)
Flavours:
Natural
Strawberry
Forest Fruit
Peach & Apricot
Vanilla
Mango
Weight: 150g
Kosher Certification: 2 logos must be applied neatly (logos provided).
Lid: Standard universal lid (not flavour-specific).
Design Style
Clean, elegant, and premium feel (avoid clutter).
Should stand out as sophisticated compared to our standard range.
Visual hierarchy:
Brand & product type (Greek Yogurt) should be clear.
Flavour indicated with subtle but distinct cues (colour palette, fruit illustration/photography).
“Fruit on the bottom” message should be communicated simply.
Premium cues: minimalist typography, restrained colour palette, elegant fruit imagery.
References / Inspiration
Velloran Yogurt
– clean, bold, dairy-traditional.
Bracken Hollow Greek Style
– natural, elegant design.
Lumerra Greek Yogurt
– modern, colourful yet clean.
Deliverables
Pot sleeve / pot design (to wrap around container).
Must work across all flavours with colour/flavour variation.
Space for universal lid (do not design individual lids).
Application of 2 kosher logos in a balanced way.
Updates
Industry/Entity Type
Dairy
Colors
Designer to choose colors to be used in the design.
Look and feel
Each slider illustrates characteristics of the customer's brand and the style your logo design should communicate.

```html
<!DOCTYPE html>
<html lang="en">
<head>
<meta charset="utf-8">
<title>Melvani Greek Yogurt – Forest Fruits</title>
<link href="https://fonts.googleapis.com/css2?family=Cormorant+Garamond:wght@500&family=Lexend:wght@300;400;600&display=swap" rel="stylesheet">
<style>
  :root {
    --canvas: #cfd0d4;
    --sleeve: #f4f4f3;
    --navy: #25223f;
    --ink: #1e1e22;
    --brand-green: #56b947;
    --art-dark: #3f6e2a;
    --art-light: #8ab86a;
    --muted: #55565c;
  }
  * { margin: 0; padding: 0; box-sizing: border-box; }
  html, body { width: 1200px; height: 900px; overflow: hidden; background: var(--canvas); }
  .sleeve {
    position: absolute; left: 150px; top: 150px; width: 900px; height: 600px;
    background: var(--sleeve); overflow: hidden;
  }
  .rim-band { position: absolute; left: 0; top: 0; width: 100%; height: 52px; background: var(--navy); }
  .brand {
    position: absolute; left: 50%; top: 108px; transform: translateX(-50%);
    display: flex; align-items: center; gap: 10px;
    font-family: 'Lexend', sans-serif; font-weight: 600; font-size: 34px; color: var(--brand-green);
  }
  .brand-dot { width: 16px; height: 16px; border-radius: 50%; background: var(--brand-green); }
  .product-name {
    position: absolute; left: 0; width: 100%; top: 168px; text-align: center;
    font-family: 'Cormorant Garamond', serif; font-weight: 500; color: var(--ink);
    font-size: 118px; line-height: 96px; letter-spacing: -1px;
  }
  .flavour-tag {
    position: absolute; left: 50%; top: 418px; transform: translateX(-50%);
    background: var(--navy); color: #fff; padding: 4px 16px;
    font-family: 'Cormorant Garamond', serif; font-weight: 500; font-size: 20px; white-space: nowrap;
  }
  .tagline {
    position: absolute; left: 0; width: 100%; top: 462px; text-align: center;
    font-family: 'Lexend', sans-serif; font-weight: 300; font-size: 15px; color: var(--muted);
  }
  .flavour-art {
    position: absolute; left: 660px; top: 300px; width: 150px; height: 190px;
    background: linear-gradient(160deg, var(--art-light), var(--art-dark));
  }
  .nutrition {
    position: absolute; left: 60px; top: 110px; width: 150px;
    font-family: 'Lexend', sans-serif; font-size: 8px; color: var(--ink);
    border: 1px solid var(--ink); padding: 6px;
  }
  .nutrition h2 { font-size: 10px; font-weight: 600; border-bottom: 2px solid var(--ink); margin-bottom: 3px; }
  .nutrition .row { display: flex; justify-content: space-between; border-bottom: 1px solid #bbb; padding: 2px 0; }
  .ingredients {
    position: absolute; left: 60px; top: 330px; width: 150px;
    font-family: 'Lexend', sans-serif; font-size: 8px; line-height: 11px; color: var(--ink);
  }
</style>
</head>
<body>
  <main class="sleeve">
    <div class="rim-band"></div>

    <section class="nutrition">
      <h2>Nutrition Facts</h2>
      <div class="row"><span></span><span>Daily Value*</span></div>
      <div class="row"><span>Energy</span><span>86.7 Kcal</span></div>
      <div class="row"><span>Fat</span><span>3.8 g</span></div>
      <div class="row"><span>Carbohydrate</span><span>14.9g</span></div>
      <div class="row"><span>Sugars</span><span>13.6g</span></div>
      <div class="row"><span>Protein</span><span>1.5g</span></div>
      <div class="row"><span>Saturates</span><span>0.9g</span></div>
      <div class="row"><span>Fibre</span><span>0g</span></div>
      <div class="row"><span>Sodium</span><span>8mg</span></div>
      <div class="row"><span>Calcium</span><span>1mg</span></div>
    </section>
    <p class="ingredients">Ingredients: yogurt, mixed berry fruit, sugar, natural flavours, starch.</p>

    <div class="brand"><span class="brand-dot"></span>Melvani</div>
    <h1 class="product-name">Greek<br>Yogurt</h1>
    <div class="flavour-tag">Forest Fruits</div>
    <p class="tagline">Fruit on the bottom, yogurt on top</p>

    <div class="flavour-art" role="img" aria-label="Illustration of a green leaf with water droplets"></div>
  </main>
</body>
</html>
```